24x24 12x12 Building Signage

https://www.thorntonpipeworks.example/
http://www.clearpathsites.example/
Looking to revamp the side of our building advertising to include both sister companies Thornton Plumbing Heating and Air Conditioning and Clearpath Sites Group. We would like a sign to grab drivers attention on a busy street. Thornton is a certified vantor dealer ( badge included) who services heating and cooling systems, plumbing services and 24/7 emergency service. Clearpath sites group is a single source solution for Facility Management, Maintenance Services and all of your buildings needs. We are open to splitting Thornton into a 12x12 and Clearpath into a 12x12 or having a creative look to merging both for a 24x24. Old signage on side of the building included in the photos.

Designs look the same

```html
<!DOCTYPE html>
<html lang="en">
<head>
<meta charset="utf-8">
<title>Thornton &amp; Clearpath Building Sign</title>
<link rel="stylesheet" href="https://fonts.googleapis.com/css2?family=Montserrat:wght@700;800;900&display=swap">
<style>
  :root {
    --page-bg: #d9d9d6;
    --brand-blue: #0a6fd8;
    --ink: #000000;
    --paper: #ffffff;
    --accent-blue: #3b55b5;
    --logo-ink: #222222;
  }
  * { box-sizing: border-box; margin: 0; padding: 0; }
  html, body { width: 1200px; height: 900px; overflow: hidden; }
  body {
    background: var(--page-bg);
    font-family: "Montserrat", sans-serif;
    position: relative;
  }
  .sign {
    position: absolute;
    left: 50px; top: 180px;
    width: 1100px; height: 540px;
    display: flex;
    box-shadow: 0 4px 14px rgba(0,0,0,0.18);
  }
  .panel-service {
    width: 526px;
    background: var(--brand-blue);
    position: relative;
    color: var(--paper);
    overflow: hidden;
  }
  .headline-hours {
    position: absolute;
    left: 38px; top: 40px;
    font-size: 168px;
    font-weight: 900;
    letter-spacing: -6px;
    line-height: 1;
    white-space: nowrap;
  }
  .headline-hours .slash { color: var(--ink); }
  .service-list {
    position: absolute;
    left: 40px; top: 232px;
    list-style: none;
    font-size: 52px;
    font-weight: 800;
    line-height: 54px;
    letter-spacing: -0.5px;
  }
  .service-list .mark { color: var(--ink); }
  .brand-thornton {
    position: absolute;
    right: 38px; bottom: 40px;
    display: flex; align-items: center; gap: 12px;
    font-size: 40px; font-weight: 800;
    color: var(--paper);
  }
  .brand-thornton .dot {
    width: 24px; height: 24px; border-radius: 50%;
    background: var(--ink);
  }
  .panel-facilities {
    flex: 1;
    background: var(--paper);
    position: relative;
  }
  .offer-stack {
    position: absolute;
    left: 35px; top: 34px;
    list-style: none;
    display: flex; flex-direction: column; gap: 7px;
  }
  .offer-stack li {
    width: 402px; height: 110px;
    background: var(--ink);
    color: var(--paper);
    font-size: 44px; font-weight: 800;
    line-height: 42px;
    padding: 13px 16px;
    letter-spacing: -0.5px;
  }
  .brand-clearpath {
    position: absolute;
    right: 36px; bottom: 30px;
    display: flex; flex-direction: column; align-items: center; gap: 8px;
    font-size: 20px; font-weight: 700;
    line-height: 24px;
    color: var(--logo-ink);
    text-align: center;
  }
  .brand-clearpath .dot {
    width: 30px; height: 30px; border-radius: 50%;
    background: var(--accent-blue);
  }
</style>
</head>
<body>
  <section class="sign">
    <div class="panel-service">
      <div class="headline-hours">24<span class="slash">/</span>7</div>
      <ul class="service-list">
        <li>HEATING<span class="mark">?</span></li>
        <li>COOLING<span class="mark">?</span></li>
        <li>PLUMBING<span class="mark">?</span></li>
      </ul>
      <div class="brand-thornton"><span class="dot"></span>Thornton</div>
    </div>
    <div class="panel-facilities">
      <ul class="offer-stack">
        <li>FACILITY<br>MANAGEMENT</li>
        <li>MAINTENANCE<br>SERVICES</li>
        <li>BUILDING<br>NEEDS</li>
      </ul>
      <div class="brand-clearpath">
        <span>clearpath<br>sites<br>group, inc.</span>
        <span class="dot"></span>
      </div>
    </div>
  </section>
</body>
</html>
```